Real Estate Entrepreneur needs a business card

I am a real estate entrepreneur, I buy houses for investment purposes, I act as a real estate agent representing buyers and sellers in residential home transactions, I am a contractor that does a wide range of home repairs and construction. I'd like a design that can stick with me through the years as my business grows and morphs to fit any niche I decide to pursue as markets change.

Target Market(s)

Anyone with interest that may be related to real estate.

Industry/Entity Type

Real Estate

Contact Information for Business Card

A card that stands out and doesn't put me in any one box. My business will evolve over time and I need a card that can stay relevant.

Colors

Designer to choose colors to be used in the design.

Requirements
Must have
• Character
Nice to have
• I'm open
Should not have
• Cliche houses and hammers

```html
<!DOCTYPE html>
<html lang="en">
<head>
<meta charset="utf-8">
<title>Miles Carter — Business Card</title>
<link rel="stylesheet" href="https://fonts.googleapis.com/css2?family=Oswald:wght@500&family=Lato:wght@400&display=swap">
<style>
  :root {
    --page-bg: #2e2e2e;
    --card-bg: #282828;
    --foil-dark: #b4845f;
    --foil-light: #f4dfc4;
    --foil-mid: #d7ae8a;
  }
  html, body {
    margin: 0;
    padding: 0;
    width: 1200px;
    height: 1200px;
    overflow: hidden;
    background: var(--page-bg);
  }
  .canvas {
    position: relative;
    width: 1200px;
    height: 1200px;
  }
  .card {
    position: absolute;
    top: 300px;
    width: 390px;
    height: 600px;
    background: var(--card-bg);
    overflow: hidden;
  }
  .card--front { left: 161px; }
  .card--back { left: 660px; }

  .foil {
    background: linear-gradient(90deg, var(--foil-dark) 0%, var(--foil-mid) 35%, var(--foil-light) 70%, var(--foil-mid) 100%);
    -webkit-background-clip: text;
    background-clip: text;
    color: transparent;
  }
  .name {
    position: absolute;
    left: 0;
    right: 0;
    margin: 0;
    text-align: center;
    white-space: nowrap;
    font-family: 'Oswald', sans-serif;
    font-weight: 500;
    font-size: 56px;
    line-height: 1;
    letter-spacing: 2px;
    text-transform: uppercase;
  }
  .role {
    position: absolute;
    left: 0;
    right: 0;
    margin: 0;
    text-align: center;
    white-space: nowrap;
    font-family: 'Lato', sans-serif;
    font-weight: 400;
    font-size: 32px;
    line-height: 1;
    letter-spacing: -0.5px;
    text-transform: uppercase;
  }
  .card--front .name { top: 104px; }
  .card--front .role { top: 178px; }
  .card--back .name { top: 210px; }
  .card--back .role { top: 284px; }

  .contact-list {
    position: absolute;
    left: 30px;
    top: 326px;
    margin: 0;
    padding: 0;
    list-style: none;
  }
  .contact-item {
    display: flex;
    align-items: center;
    height: 44px;
    white-space: nowrap;
    font-family: 'Lato', sans-serif;
    font-size: 28px;
    letter-spacing: 0.3px;
  }
  .contact-icon {
    width: 30px;
    height: 30px;
    margin-right: 24px;
    flex: none;
  }
  .contact-icon * {
    fill: none;
    stroke: var(--foil-dark);
    stroke-width: 1.6;
    stroke-linecap: round;
    stroke-linejoin: round;
  }
</style>
</head>
<body>
<main class="canvas">
  <section class="card card--front">
    <h1 class="name foil">Miles Carter</h1>
    <p class="role foil">Manager</p>
    <ul class="contact-list">
      <li class="contact-item">
        <svg class="contact-icon" viewBox="0 0 30 30" aria-hidden="true">
          <path d="M8 4 L12 9 L10 12 C11 16 14 19 18 20 L21 18 L26 22 L23 26 C14 26 4 16 4 7 Z"/>
          <path d="M16 8 A6 6 0 0 1 22 14"/>
          <path d="M16 3 A11 11 0 0 1 27 14"/>
        </svg>
        <span class="foil">(+88) 01987654320</span>
      </li>
      <li class="contact-item">
        <svg class="contact-icon" viewBox="0 0 30 30" aria-hidden="true">
          <rect x="2" y="7" width="26" height="17"/>
          <path d="M2 7 L15 17 L28 7"/>
          <path d="M2 24 L12 15 M28 24 L18 15"/>
        </svg>
        <span class="foil">info@milescarter.com</span>
      </li>
      <li class="contact-item">
        <svg class="contact-icon" viewBox="0 0 30 30" aria-hidden="true">
          <circle cx="15" cy="15" r="12"/>
          <ellipse cx="15" cy="15" rx="5" ry="12"/>
          <path d="M3 15 H27 M5 9 H25 M5 21 H25 M15 3 V27"/>
        </svg>
        <span class="foil">www.milescarter.com</span>
      </li>
    </ul>
  </section>

  <section class="card card--back">
    <h2 class="name foil">Miles Carter</h2>
    <p class="role foil">Manafer</p>
  </section>
</main>
</body>
</html>
```